Ecommerce Web Design - We currently have a live website running on https://www.brivanto.co.za - this website must be redesigned for an eCommerce website since we are moving to sell our items online. Kindly put a new design utilising the information from the current live website

Link to Pictures & Brochure: https://tolvesta-my.filedrop.example/:f:/g/personal/dumisa_paterlo_co_za/QxpLMrtVwaUeHbnKd3ZPoeyT-RUI8gHjNtwXZCF7pBLAmv?e=kR4z91

```html
<!DOCTYPE html>
<html lang="en">
<head>
<meta charset="utf-8">
<title>Brivanto Ladders — Ecommerce Homepage</title>
<link href="https://fonts.googleapis.com/css2?family=Lexend:wght@300;400;500;600;700&display=swap" rel="stylesheet">
<style>
:root{
  --red:#e50914;
  --ink:#161616;
  --grey:#6f6f6f;
  --soft:#efefef;
  --line:#d9d9d9;
  --teal-a:#0c5b7a;
  --teal-b:#0e7699;
  --dark:#262626;
  --green:#1faa3a;
  --star:#f3b400;
  --worker:#2c4f86;
  --tan:#b89a73;
  --ladder-y:#f2c418;
  --ladder-o:#f07a1a;
  --silver:#c9ced6;
}
*{box-sizing:border-box;margin:0;padding:0}
html,body{width:1200px;height:675px;overflow:hidden}
body{font-family:'Lexend',sans-serif;color:var(--ink);
  background:radial-gradient(ellipse at 40% 30%,var(--teal-b),var(--teal-a) 75%);position:relative}
.red{color:var(--red)}

/* ===== Desktop view ===== */
.desk{position:absolute;left:62.5px;top:109px;width:790px;height:566px;background:#fff;overflow:hidden}
.topbar{height:27.5px;background:var(--soft);display:flex;align-items:center;padding:0 38px;font-size:8.4px;color:#555;font-weight:300}
.topbar .item{display:flex;align-items:center;gap:4px;margin-right:13px}
.topbar .note{margin-left:auto}
.topbar .note u{color:#888}
.topbar svg{width:10px;height:10px}
.header{position:absolute;top:27.5px;left:0;right:0;height:66.5px;border-bottom:1.5px solid #333}
.brand{position:absolute;display:flex;align-items:center;gap:9px}
.brand .mark{width:26px;height:26px;background:var(--red)}
.brand .name{font-weight:600;font-size:9.4px;line-height:15.5px;color:var(--ink)}
.search{position:absolute;left:253px;top:19.5px;width:254px;height:26px;background:#f2f2f2;border-radius:3px;display:flex;align-items:center;font-size:8.8px;color:#8a8a8a;font-weight:300;padding-left:9px}
.search .btn{position:absolute;right:0;top:0;width:30px;height:26px;background:#e4e4e4;border-radius:0 3px 3px 0;display:flex;align-items:center;justify-content:center}
.acct{position:absolute;top:19px;display:flex;align-items:center;gap:5px;font-size:8.9px;line-height:11.5px;color:#333}
.acct b{font-weight:400;color:var(--ink)}
.acct span{color:#666;font-weight:300}
.nav{position:absolute;top:104px;left:38px;right:39px;height:27px;display:flex;gap:21px;font-size:10px;color:#8a8a8a;border-bottom:2px solid var(--red)}
.nav a{text-decoration:none;color:inherit}
.nav a.on{color:var(--ink);font-weight:500;border-bottom:2.5px solid var(--ink);margin-bottom:-2.5px;padding:0 11px}
.hero{position:absolute;left:38px;top:161px;width:713px;height:283px;border-radius:4px;overflow:hidden}
.hero .photo{position:absolute;inset:0;
  background:linear-gradient(100deg,#c9ccd3 0%,#dcdfe5 30%,#b8c1d2 46%,var(--worker) 58%,#c2a888 66%,#e8e9ec 74%,#f4f4f6 84%,#eee9d2 92%,#e6e8ec 100%)}
.hero h1{position:absolute;left:27px;top:24px;font-size:20px;line-height:33px;font-weight:600;letter-spacing:-.1px}
.hero p{position:absolute;left:27px;top:137px;width:272px;font-size:10px;line-height:15.5px;color:#222}
.hero .cta{position:absolute;left:27px;top:192px;width:102px;height:33px;background:var(--red);color:#fff;font-size:11.2px;font-weight:500;display:flex;align-items:center;justify-content:center}
.promo{position:absolute;left:38px;top:469px;width:713px;height:71px;border:1px solid #444;display:flex;align-items:center}
.promo .brand{position:static;margin-left:12px}
.promo .msg{position:absolute;left:155px;font-size:16px;font-weight:600;letter-spacing:-.1px}
.promo .cta{position:absolute;left:597px;top:19px;width:96px;height:32px;background:var(--red);color:#fff;font-size:10.8px;font-weight:500;display:flex;align-items:center;justify-content:center}

/* ===== Full page preview ===== */
.page{position:absolute;left:899px;top:0;width:239px;height:675px;background:#fff;overflow:hidden;font-size:3.2px;color:#333}
.page .t{position:absolute;white-space:nowrap}
.p-brand{display:flex;align-items:center;gap:3px;font-weight:600;font-size:2.6px;line-height:3.6px}
.p-brand i{width:8px;height:8px;background:var(--red);display:block}
.p-search{left:76px;top:13px;width:77px;height:8px;background:#f2f2f2;border-radius:1px;font-size:2.6px;color:#999;padding:2.6px 3px}
.p-nav{left:15px;top:32px;width:209px;border-bottom:.8px solid var(--red);display:flex;gap:7px;font-size:2.6px;color:#777;padding-bottom:3.5px}
.p-nav b{color:#111;font-weight:500}
.p-hero{left:12px;top:49px;width:215px;height:85px;border-radius:1px;
  background:linear-gradient(100deg,#c9ccd3 0%,#dcdfe5 34%,#b8c1d2 48%,var(--worker) 60%,#c2a888 68%,#e8e9ec 76%,#f4f4f6 86%,#eee9d2 93%,#e6e8ec 100%)}
.p-hero h2{position:absolute;left:8px;top:8px;font-size:5.3px;line-height:10px;font-weight:600;color:#111;white-space:nowrap}
.p-hero .s{position:absolute;left:8px;top:42px;width:82px;font-size:2.4px;line-height:3.6px;white-space:normal}
.p-btn{position:absolute;background:var(--red);color:#fff;font-size:2.4px;display:flex;align-items:center;justify-content:center;white-space:nowrap}
.p-box{left:12px;top:142px;width:215px;height:21px;border:.6px solid #555;display:flex;align-items:center;padding-left:4px}
.p-box .m{position:absolute;left:47px;font-size:3.9px;font-weight:600;color:#111}
.p-h{font-size:5.4px;font-weight:600;color:#111}
.p-tile{position:absolute;top:201px;height:46px}
.card{position:absolute;width:49px}
.card .img{height:60px;position:relative}
.card .img span{position:absolute;left:2px;bottom:2px;background:var(--green);color:#fff;font-size:2px;padding:.6px 1.6px}
.g-silver{background:linear-gradient(180deg,#f7f8fa 0%,var(--silver) 50%,#f4f5f7 100%)}
.g-yellow{background:linear-gradient(180deg,#fbf2c4 0%,var(--silver) 45%,#f4f5f7 100%)}
.g-orange{background:linear-gradient(180deg,#fde1c8 0%,var(--ladder-o) 50%,#f6e8dc 100%)}
.price{font-size:3.2px;font-weight:600;color:var(--red);margin-top:4px}
.nm{font-size:2.3px;color:#444;margin-top:2px}
.stars{color:var(--star);font-size:2.6px;letter-spacing:.2px;line-height:3px}
.cat{position:absolute;width:51px;height:20px;background:#f4f5f7;font-size:2.5px;line-height:3.2px;padding:4px 3px;color:#333}
.cat .pic{position:absolute;right:3px;top:3px;width:14px;height:14px;border-radius:1px}
.cat.on{background:var(--red);color:#fff}
.deal{position:absolute;top:527px;width:69px}
.deal .img{height:45px;position:relative}
.deal .img em{position:absolute;left:3px;top:3px;background:var(--star);color:#fff;font-size:1.8px;font-style:normal;padding:.5px 1.5px}
.d-y{background:linear-gradient(180deg,#f6f1dc 0%,var(--ladder-y) 40%,#e9d48c 60%,var(--tan) 61%,#a88558 100%)}
.d-r{background:linear-gradient(180deg,#f8e2dc 0%,#e94a2a 40%,#e9a58c 60%,var(--tan) 61%,#a88558 100%)}
.d-b{background:linear-gradient(180deg,#eef0dc 0%,#d9c23a 35%,#6f86b0 55%,var(--tan) 61%,#a88558 100%)}
.deal .row{display:flex;gap:3px;align-items:baseline;margin-top:4px;font-size:2.8px;font-weight:600}
.deal .row s{color:#aaa;font-weight:400}
.deal .add{position:absolute;right:0;top:63px;background:var(--green);color:#fff;font-size:2px;padding:.8px 2px}
.foot{position:absolute;left:0;top:616px;width:239px;height:59px;background:var(--dark);color:#ddd;font-size:2.2px;line-height:3.4px}
.foot .t{color:#ccc}
.foot b{color:#fff;font-weight:500}
.heart{position:absolute;right:3px;top:3px;width:4px;height:4px}
</style>
</head>
<body>

<section class="desk" aria-label="Homepage, desktop">
  <div class="topbar">
    <div class="item"><svg viewBox="0 0 24 24" fill="none" stroke="#666" stroke-width="1.6"><path d="M5 3h4l2 5-2.5 1.5a11 11 0 0 0 6 6L16 13l5 2v4a2 2 0 0 1-2 2A17 17 0 0 1 3 5a2 2 0 0 1 2-2z"/></svg>+27 100 555 0148</div>
    <div class="item"><svg viewBox="0 0 24 24" fill="none" stroke="#666" stroke-width="1.6"><path d="M5 3h4l2 5-2.5 1.5a11 11 0 0 0 6 6L16 13l5 2v4a2 2 0 0 1-2 2A17 17 0 0 1 3 5a2 2 0 0 1 2-2z"/></svg>+27 100 555 0149</div>
    <div class="item"><svg viewBox="0 0 24 24" fill="none" stroke="#666" stroke-width="1.6"><rect x="3" y="5" width="18" height="14" rx="2"/><path d="M3 7l9 6 9-6"/></svg>Contact@brivanto.com</div>
    <div class="note">We Deliver All Accross South Africa. <u>Learn more</u></div>
  </div>

  <header class="header">
    <div class="brand" style="left:41px;top:17px">
      <span class="mark"></span>
      <span class="name">BRIVANTO<br>LADDERS</span>
    </div>
    <div class="search">What Can We Help You Find?
      <span class="btn"><svg width="13" height="13" viewBox="0 0 24 24" fill="none" stroke="#e50914" stroke-width="1.8"><circle cx="11" cy="11" r="7"/><path d="M16 16l5 5"/></svg></span>
    </div>
    <div class="acct" style="left:563px">
      <svg width="22" height="22" viewBox="0 0 24 24" fill="none" stroke="#e50914" stroke-width="1.6"><circle cx="12" cy="12" r="10"/><circle cx="12" cy="10" r="3.5"/><path d="M5.5 19c1.5-3 4-4 6.5-4s5 1 6.5 4"/></svg>
      <div><b>Hi There!</b><br><span>Sign Up | Log In</span></div>
    </div>
    <div class="acct" style="left:684px">
      <svg width="22" height="22" viewBox="0 0 24 24" fill="none" stroke="#e50914" stroke-width="1.6"><path d="M3 9h18l-2 11H5z"/><path d="M8 9l4-6 4 6"/><path d="M9 13v4M15 13v4"/></svg>
      <div><b>Your Cart</b><br><span>0 Items</span></div>
    </div>
  </header>

  <nav class="nav">
    <a class="on">Home</a><a>Products</a><a>Categories</a><a>Safety Information</a><a>Delivery</a><a>About Us</a><a>Contact</a>
  </nav>

  <div class="hero">
    <div class="photo" role="img" aria-label="Photo of a worker in a blue cap and shirt kneeling with a drill beside a toolbox, with a yellow-topped aluminium step ladder on a pale grey floor"></div>
    <h1>South Africa <span class="red">Leading Manufacturer</span><br>Of Ladders, Trolleys, Castors, and<br>Ladder Accessories</h1>
    <p>From Step Ladders To Extention Ladders, Platform Ladders, Trolleys To Order Pickers And Everything In Between, We'ill Deliver All Your Ladder Needs.</p>
    <div class="cta">Shop Now</div>
  </div>

  <div class="promo">
    <div class="brand"><span class="mark"></span><span class="name">BRIVANTO<br>LADDERS</span></div>
    <div class="msg">FREE DELIVERY ON ALL PURCHASES OVER : <span class="red">8000 ZAR</span></div>
    <div class="cta">Shop Now</div>
  </div>
</section>

<section class="page" aria-label="Homepage, full length">
  <div class="t" style="left:15px;top:3px;font-size:2px;color:#888">+27 100 555 0148 &nbsp; +27 100 555 0149 &nbsp; Contact@brivanto.com</div>
  <div class="t" style="right:10px;top:3px;font-size:2px;color:#888">We Deliver All Accross South Africa. Learn more</div>
  <div class="t p-brand" style="left:14px;top:13px"><i></i>BRIVANTO<br>LADDERS</div>
  <div class="t p-search">What Can We Help You Find?</div>
  <div class="t" style="left:170px;top:14px;font-size:2.2px;line-height:3px">Hi There!<br>Sign Up | Log In</div>
  <div class="t" style="left:204px;top:14px;font-size:2.2px;line-height:3px">Your Cart<br>0 Items</div>
  <div class="t p-nav"><b>Home</b><span>Products</span><span>Categories</span><span>Safety Information</span><span>Delivery</span><span>About Us</span><span>Contact</span></div>

  <div class="t p-hero" role="img" aria-label="Hero photo of a worker with a drill beside a step ladder">
    <h2>South Africa <span class="red">Leading Manufacturer</span><br>Of Ladders, Trolleys, Castors, and<br>Ladder Accessories</h2>
    <div class="s">From Step Ladders To Extention Ladders, Platform Ladders, Trolleys To Order Pickers And Everything In Between, We'ill Deliver All Your Ladder Needs.</div>
    <div class="p-btn" style="left:8px;top:62px;width:25px;height:9px">Shop Now</div>
  </div>

  <div class="t p-box">
    <div class="p-brand"><i></i>BRIVANTO<br>LADDERS</div>
    <div class="m">FREE DELIVERY ON ALL PURCHASES OVER : <span class="red">8000 ZAR</span></div>
    <div class="p-btn" style="left:196px;top:5px;width:15px;height:8px">Shop Now</div>
  </div>

  <div class="t p-h" style="left:12px;top:184px">Discover Our <span class="red">Best Selling</span> Products</div>
  <div class="p-tile" style="left:11px;width:122px;background:linear-gradient(100deg,#fff 0%,#fff 45%,#f7c430 62%,#f08a1a 72%,#fff 85%),#fff" role="img" aria-label="Fibreglass ladder range promotion with orange ladder">
    <div style="position:absolute;left:0;right:0;bottom:0;height:20px;background:linear-gradient(180deg,#a9a9a9,#8d8d8d)"></div>
    <div class="t" style="left:5px;top:8px;font-size:3.2px;font-weight:600;color:var(--red);line-height:4.6px">FIBERGLASS<br>LADDERS RANGE</div>
    <div class="t" style="left:8px;top:23px;background:#111;color:#fff;font-size:2.8px;padding:.8px 3px">15% OFF</div>
  </div>
  <div class="p-tile" style="left:138px;width:89px;background:linear-gradient(180deg,#2a2a2a,#0c0c0c)" role="img" aria-label="Ladder accessories promotion with hooks and brackets">
    <div class="t" style="left:34px;top:23px;font-size:2.6px;color:#fff;font-weight:500">LADDERS ACCESSORIES</div>
    <div class="p-btn" style="left:42px;top:31px;width:15px;height:6px;font-size:2px">Shop Now</div>
  </div>

  <div class="card" style="left:11px;top:253px"><div class="img g-silver" role="img" aria-label="Aluminium step ladder"><span>+ ADD</span></div><div class="price">1450 ZAR</div><div class="nm">Ap- Range Household</div><div class="stars">★★★★★</div></div>
  <div class="card" style="left:67px;top:253px"><div class="img g-silver" role="img" aria-label="Aluminium step ladder"><span>+ ADD</span><svg class="heart" viewBox="0 0 10 10"><path d="M5 9L1 5a2.2 2.2 0 0 1 4-3 2.2 2.2 0 0 1 4 3z" fill="#e50914"/></svg></div><div class="price">2840 ZAR</div><div class="nm">ISL Range Ladder</div><div class="stars">★★★★★</div></div>
  <div class="card" style="left:122px;top:253px"><div class="img g-yellow" role="img" aria-label="Aluminium step ladder with yellow top"><span>+ ADD</span></div><div class="price">2840 ZAR</div><div class="nm">ISL Range Ladder</div><div class="stars">★★★★★</div></div>
  <div class="card" style="left:178px;top:253px"><div class="img g-orange" role="img" aria-label="Orange fibreglass ladder"><span>+ ADD</span></div><div class="price">5640 ZAR</div><div class="nm">Fiberglass Heavy Duty Ladder</div><div class="stars">★★★★★</div></div>
  <div class="p-btn" style="left:93px;top:342px;width:53px;height:9px;background:#111">Discover All Our Products</div>

  <div class="t p-h" style="left:0;width:239px;text-align:center;top:372px">Shop By <span class="red">Category</span></div>
  <div class="cat" style="left:12px;top:390px">Access Equipement<div class="pic g-silver" role="img" aria-label="Access platform"></div></div>
  <div class="cat" style="left:67px;top:390px">Aluminium<br>Ladders<div class="pic g-silver" role="img" aria-label="Aluminium ladder"></div></div>
  <div class="cat on" style="left:122px;top:390px">Fiberglass<br>Ladders<div class="pic" style="background:linear-gradient(180deg,#ff9a6a,#f5c640)" role="img" aria-label="Fibreglass ladders"></div></div>
  <div class="cat" style="left:176px;top:390px">Castor Wheels<div class="pic" style="background:linear-gradient(180deg,#d6d8dc,#3a3a3a)" role="img" aria-label="Castor wheel"></div></div>
  <div class="cat" style="left:12px;top:415px">Storage<br>Equipements<div class="pic" style="background:linear-gradient(180deg,#6a6a6a,#2a2a2a)" role="img" aria-label="Storage bins"></div></div>
  <div class="cat" style="left:67px;top:415px">Ladders<br>Accessories<div class="pic" style="background:linear-gradient(180deg,#eceef1,#aeb3ba)" role="img" aria-label="Ladder hooks"></div></div>
  <div class="cat" style="left:122px;top:415px">Trolleys<div class="pic" style="background:linear-gradient(180deg,#e7ebf2,#8ea3c4)" role="img" aria-label="Hand trolley"></div></div>

  <div class="t" style="left:12px;top:447px;width:215px;height:42px;background:linear-gradient(90deg,#111 0%,#1e1e1e 52%,var(--red) 52%,var(--red) 54%,#dfe2e8 55%,#c3cbd8 72%,var(--worker) 78%,#e6e8ec 84%,#eee8cf 94%,#e6e8ec 100%)" role="img" aria-label="Banner with worker and step ladder">
    <div class="t" style="left:5px;top:6px;font-size:4.6px;line-height:9.6px;font-weight:600;color:#fff"><span class="red">Welcome</span> To the Ladder<br>Shop, We Cover <span class="red">All Types</span><br>Of Ladders</div>
    <div class="p-btn" style="left:56px;top:28px;width:27px;height:6px;font-size:2px">Download Catalogue</div>
  </div>

  <div class="t p-h" style="left:12px;top:509px">Our <span class="red">Deal</span> Of The Day</div>
  <div class="deal" style="left:12px"><div class="img d-y" role="img" aria-label="Yellow fibreglass ladder"><em>SALE</em></div><div class="row"><s>2450 ZAR</s><span class="red">2150 ZAR</span></div><div class="nm">Ap- Range Household</div><div class="stars">★★★★★</div><span class="add">+ ADD</span></div>
  <div class="deal" style="left:85px"><div class="img d-r" role="img" aria-label="Red fibreglass ladder"><em>SALE</em></div><div class="row"><s>3925 ZAR</s><span class="red">3200 ZAR</span></div><div class="nm">Ap- Range Household</div><div class="stars">★★★★★</div><span class="add">+ ADD</span></div>
  <div class="deal" style="left:158px"><div class="img d-b" role="img" aria-label="Yellow and blue fibreglass ladder"><em>SALE</em></div><div class="row"><s>6500 ZAR</s><span class="red">5850 ZAR</span></div><div class="nm">Ap- Range Household</div><div class="stars">★★★★★</div><span class="add">+ ADD</span></div>

  <footer class="foot">
    <div class="t p-brand" style="left:20px;top:8px;color:#fff"><i></i>BRIVANTO<br>LADDERS</div>
    <div class="t" style="left:20px;top:28px">From Step Ladders To Extention<br>Ladders, Platform Ladders, Trolleys<br>To Order Pickers And Everything In<br>Between.</div>
    <div class="t" style="left:94px;top:9px"><b>Browse</b><br>Home<br>Products<br>Safety<br>Categories<br>Delivery</div>
    <div class="t" style="left:130px;top:9px"><b>Customer Service</b><br>Take Your Order<br>Easy Returns<br>Shipping &amp; Pickup<br>Warranty<br>Services</div>
    <div class="t" style="left:179px;top:9px"><b>Contact Us</b><br>+27 100 555 0148<br>contact@brivanto.com<br><b>Follow Us</b></div>
    <div class="t" style="left:20px;top:53px;font-size:1.9px">© copyrighted, Brivanto Ladders 2022</div>
    <div class="t" style="left:148px;top:53px;font-size:1.9px">Return Policy &nbsp;| Privacy Policy &nbsp;| Terms &amp; Conditions</div>
  </footer>
</section>

</body>
</html>
```